Need DL Flyer for Real Estate Drops

We need a real estate flyer ,double sided. With content on 1 side like: Want to know what's your house is worth " contact us today and on other side agent details. We are looking for an ongoing partnership with designer so this assignment will be ongoing

```html
<!DOCTYPE html>
<html lang="en">
<head>
<meta charset="utf-8">
<title>Meridian Real Estate – DL Flyer</title>
<link rel="stylesheet" href="https://fonts.googleapis.com/css2?family=Inter:wght@400;500;700&family=Oswald:wght@600;700&family=Great+Vibes&display=swap">
<style>
:root{
  --navy:#0b1630;
  --navy-soft:#1c2a4a;
  --red:#d0222a;
  --red-dark:#a8151c;
  --white:#ffffff;
  --ink:#0e1a36;
  --stage:#b7b7b7;
  --slate:#7c8597;
  --grass:#6c9a3c;
}
*{margin:0;padding:0;box-sizing:border-box}
html,body{width:1193px;height:1200px;overflow:hidden}
body{background:var(--stage);position:relative;font-family:"Inter",Arial,sans-serif}
.flyer{position:absolute;top:228px;width:354px;height:743px;overflow:hidden}
.flyer--front{left:215px;background:var(--white)}
.flyer--back{left:622px;background:var(--navy);color:var(--white)}
.brand{position:absolute;display:flex;align-items:center}
.brand__square{width:76px;height:76px;background:var(--red);border-radius:6px;margin-right:22px}
.brand__text{display:flex;flex-direction:column;align-items:center}
.brand__name{font-family:"Inter",Arial,sans-serif;font-weight:500;font-size:40px;line-height:1;letter-spacing:-0.5px}
.brand__sub{font-size:11px;letter-spacing:3.5px;margin-top:6px;font-weight:500}
.flyer--front .brand{left:41px;top:35px}
.flyer--front .brand__name,.flyer--front .brand__sub{color:var(--ink)}
.flyer--back .brand{left:52px;top:58px}
.flyer--back .brand__square{width:70px;height:70px;margin-right:18px}
.flyer--back .brand__name{color:var(--white);font-size:38px}
.flyer--back .brand__sub{color:var(--white)}
.headline{position:absolute;left:25px;top:137px;width:305px;height:182px;
  background:linear-gradient(180deg,#8a90a0 0%,#3a4560 30%,var(--navy) 55%);
  border-radius:48px 0 60px 0;text-align:center;color:var(--white);padding-top:16px}
.headline__script{font-family:"Great Vibes",cursive;font-size:44px;line-height:1}
.headline__big{font-family:"Oswald",Arial,sans-serif;font-weight:700;text-transform:uppercase;line-height:1;letter-spacing:-0.5px}
.headline__big--one{font-size:44px;margin-top:2px}
.headline__big--two{font-size:36px;margin-top:2px}
.cta{position:absolute;left:0;width:100%;top:330px;text-align:center;font-family:"Great Vibes",cursive;font-size:32px;color:var(--ink)}
.cta-pill{position:absolute;left:38px;top:364px;width:268px;height:34px;border-radius:17px;
  background:linear-gradient(180deg,#e3434a,var(--red) 50%,var(--red-dark));display:flex;align-items:center;justify-content:center;gap:6px;
  color:var(--white);font-weight:700;font-size:30px;letter-spacing:0.5px}
.cta-pill svg{width:22px;height:22px}
.house-photo{position:absolute;left:0;top:395px;width:100%;height:348px;
  background:linear-gradient(180deg,#ffffff 0%,#c9ccc8 20%,#a8aca6 55%,var(--grass) 80%,#7aa84a 100%)}
.web-band{position:absolute;left:0;top:686px;width:100%;height:35px;background:var(--navy);color:var(--white);
  font-size:17px;letter-spacing:1px;display:flex;align-items:center;justify-content:center}
.web-band b,.agent__web b{font-weight:700}
.agent{position:absolute;left:0;width:100%;text-align:center}
.agent__name{top:170px;font-family:"Oswald",Arial,sans-serif;font-weight:700;font-size:30px;color:var(--red);line-height:1}
.agent__role{top:203px;font-size:17.5px;line-height:22px}
.agent__rule{position:absolute;left:143px;top:260px;width:67px;height:2px;background:var(--red)}
.agent__address{top:272px;font-size:14.5px;line-height:18px}
.contact-icons{position:absolute;top:325px;left:100px;display:flex;gap:7px}
.contact-icons span{width:34px;height:34px;border-radius:50%;background:var(--red);display:flex;align-items:center;justify-content:center}
.contact-icons svg{width:18px;height:18px}
.agent__phone{top:370px;font-size:20px;line-height:24px;letter-spacing:0.5px}
.agent__email{top:417px;font-size:15.5px}
.agent__web{top:437px;font-size:15.5px}
.social{position:absolute;top:468px;left:147px;display:flex;gap:3px;z-index:2}
.social span{width:30px;height:30px;border-radius:50%;background:var(--red)}
.agent-photo{position:absolute;left:0;top:480px;width:100%;height:263px;
  background:linear-gradient(180deg,var(--navy) 0%,#2d3850 40%,#8c8f96 75%,#b59480 100%)}
</style>
</head>
<body>

<section class="flyer flyer--front">
  <div class="brand">
    <div class="brand__square"></div>
    <div class="brand__text"><span class="brand__name">meridian</span><span class="brand__sub">REAL ESTATE</span></div>
  </div>
  <div class="headline">
    <div class="headline__script">Want to know</div>
    <div class="headline__big headline__big--one">What's your</div>
    <div class="headline__big headline__big--two">house is worth?</div>
  </div>
  <div class="cta">Contact us today</div>
  <div class="cta-pill">
    <svg viewBox="0 0 24 24" fill="none" stroke="#fff" stroke-width="1.8"><path d="M6 3l3 4-2 2c1 3 4 6 7 7l2-2 4 3-2 3C10 21 3 14 3 5z"/></svg>
    <span>03 9000 1234</span>
  </div>
  <div class="house-photo" role="img" aria-label="Photo of a grey two-storey family home with a garden path and green lawn"></div>
  <div class="web-band">www.<b>meridianrealestate</b>.com.au</div>
</section>

<section class="flyer flyer--back">
  <div class="brand">
    <div class="brand__square"></div>
    <div class="brand__text"><span class="brand__name">meridian</span><span class="brand__sub">REAL ESTATE</span></div>
  </div>
  <div class="agent agent__name">ARJUN MEHTA</div>
  <div class="agent agent__role">Managing Director/LEA<br>Meridian Real Estate</div>
  <div class="agent__rule"></div>
  <div class="agent agent__address">14/8 Harbour Lane<br>Westfield 3030</div>
  <div class="contact-icons">
    <span><svg viewBox="0 0 24 24" fill="#fff"><path d="M6 3l3 4-2 2c1 3 4 6 7 7l2-2 4 3-2 3C10 21 3 14 3 5z"/></svg></span>
    <span><svg viewBox="0 0 24 24" fill="none" stroke="#fff" stroke-width="2"><rect x="7" y="3" width="10" height="18" rx="2"/></svg></span>
    <span><svg viewBox="0 0 24 24" fill="#fff"><path d="M3 6h18v12H3z"/><path d="M3 6l9 7 9-7" stroke="#d0222a" stroke-width="1.5" fill="none"/></svg></span>
    <span><svg viewBox="0 0 24 24" fill="none" stroke="#fff" stroke-width="2"><circle cx="12" cy="12" r="9"/><path d="M3 12h18M12 3c3 3 3 15 0 18M12 3c-3 3-3 15 0 18"/></svg></span>
  </div>
  <div class="agent agent__phone">03 9000 1234<br>0400111222</div>
  <div class="agent agent__email">arjun@meridianrealestate.com.au</div>
  <div class="agent agent__web"><b>meridianrealestate</b>.com.au</div>
  <div class="social"><span></span><span></span></div>
  <div class="agent-photo" role="img" aria-label="Black and white portrait of the agent in a suit beside a small wooden house model on a calculator"></div>
</section>

</body>
</html>
```